Architecture firm needing a business card

We need a business card design for a new company based in the US called "Pellmore Architecture". Seeking minimalist designs that have a creativity/design feel but must be clean and professional. Please refer to the logo attached.

Target Market(s)

Real Estate Investors, Home Builders and Construction Firms.

Industry/Entity Type

Architecture

Contact Information for Business Card

Standard US size business cards. Would like to have some sort of graphic on the back side of the card - nothing that is too loud but something that may catch your attention. More or less grayscale colors that are in line with the logo colors (navy and greys essentially). Additional colors maybe accepted if blended properly (earthtones), but might be difficult to accomplish and maintain the clean/minimalist look.

Requirements
Must have
• Clean Lines
Nice to have
• some sort of graphics, would like to have something creative on the back side of the card
Should not have
• nothing too busy, cluttered or overwhelming.

```html
<!DOCTYPE html>
<html lang="en">
<head>
<meta charset="utf-8">
<title>Pellmore Architecture – Business Card</title>
<link rel="stylesheet" href="https://fonts.googleapis.com/css2?family=Montserrat:wght@500&family=Arimo:wght@400&display=swap">
<style>
  :root {
    --navy: #1e4466;
    --navy-deep: #183a58;
    --paper: #f7f7f8;
    --paper-shade: #e9eaec;
    --grey: #8a8d92;
    --icon: #9a9ca0;
    --stage: #2b2b2d;
    --white: #ffffff;
  }
  * { box-sizing: border-box; margin: 0; padding: 0; }
  html, body { width: 1200px; height: 900px; overflow: hidden; }
  body {
    background: var(--stage);
    position: relative;
    font-family: "Arimo", Arial, sans-serif;
  }
  .card {
    position: absolute;
    left: 250px;
    width: 700px;
    height: 400px;
    border-radius: 22px;
    overflow: hidden;
  }

  /* Back side */
  .card-back { top: 35px; background: var(--navy); }
  .card-back .edge-band {
    position: absolute;
    height: 9px;
    background: var(--white);
    border-radius: 5px;
  }
  .card-back .edge-band.top { top: 0; left: 0; width: 92%; border-radius: 0 0 6px 0; }
  .card-back .edge-band.bottom { bottom: 0; right: 0; width: 88%; border-radius: 6px 0 0 0; }
  .card-back .brand {
    position: absolute;
    left: 0; right: 0; top: 148px;
    display: flex; align-items: center; justify-content: center; gap: 22px;
    color: var(--white);
  }
  .card-back .brand-mark { width: 70px; height: 70px; border: 6px solid var(--white); }
  .brand-text { font-family: "Montserrat", Arial, sans-serif; font-weight: 500; line-height: 1; }
  .card-back .brand-name { font-size: 52px; letter-spacing: 2px; }
  .card-back .brand-sub { font-size: 20px; letter-spacing: 9px; margin-top: 8px; }

  /* Front side */
  .card-front {
    top: 465px;
    background: linear-gradient(120deg, var(--white) 0%, var(--paper) 55%, var(--paper-shade) 100%);
  }
  .card-front .edge-band {
    position: absolute;
    height: 14px;
    background: var(--navy);
  }
  .card-front .edge-band.top { top: 0; right: 0; width: 52%; border-radius: 0 0 0 14px; }
  .card-front .edge-band.bottom { bottom: 0; right: 0; width: 72%; border-radius: 14px 0 0 0; }
  .card-front .brand {
    position: absolute; left: 34px; top: 42px;
    display: flex; align-items: center; gap: 12px;
    color: var(--navy);
  }
  .card-front .brand-mark { width: 42px; height: 42px; border: 4px solid var(--navy); }
  .card-front .brand-name { font-size: 34px; letter-spacing: 1px; }
  .card-front .brand-sub { font-size: 12.5px; letter-spacing: 6px; margin-top: 4px; }

  .person { position: absolute; right: 44px; top: 118px; text-align: right; }
  .person-name { font-size: 19px; color: var(--navy); }
  .person-role { font-size: 10px; color: var(--grey); margin-top: 2px; }
  .divider { position: absolute; height: 1px; background: var(--navy); opacity: .7; }
  .divider.name-rule { left: 250px; right: 40px; top: 166px; }
  .divider.contact-rule { left: 34px; width: 190px; top: 258px; }

  .contacts { position: absolute; left: 34px; top: 270px; list-style: none; }
  .contacts li {
    display: flex; align-items: center; gap: 12px;
    font-size: 13.5px; color: var(--navy-deep); height: 24px;
  }
  .contacts svg { width: 16px; height: 16px; fill: none; stroke: var(--icon); stroke-width: 1.6; }
</style>
</head>
<body>

<section class="card card-back" aria-label="Card back">
  <span class="edge-band top"></span>
  <span class="edge-band bottom"></span>
  <div class="brand">
    <span class="brand-mark"></span>
    <div class="brand-text">
      <div class="brand-name">PELLMORE</div>
      <div class="brand-sub">ARCHITECTURE</div>
    </div>
  </div>
</section>

<section class="card card-front" aria-label="Card front">
  <span class="edge-band top"></span>
  <span class="edge-band bottom"></span>
  <div class="brand">
    <span class="brand-mark"></span>
    <div class="brand-text">
      <div class="brand-name">PELLMORE</div>
      <div class="brand-sub">ARCHITECTURE</div>
    </div>
  </div>

  <div class="person">
    <div class="person-name">Daniel Reyes</div>
    <div class="person-role">Owner</div>
  </div>
  <span class="divider name-rule"></span>
  <span class="divider contact-rule"></span>

  <ul class="contacts">
    <li>
      <svg viewBox="0 0 16 16"><circle cx="8" cy="8" r="7"/><path d="M5.5 4.5l1.5 1.5-1 1c.6 1.3 1.7 2.4 3 3l1-1 1.5 1.5-1 1c-2.5-.5-4.5-2.5-5-5z"/></svg>
      (916) 555-0142
    </li>
    <li>
      <svg viewBox="0 0 16 16"><rect x="2" y="6" width="12" height="7" rx="1"/><path d="M5 6V2h6v4M5 10h6"/></svg>
      (916) 555-0178
    </li>
    <li>
      <svg viewBox="0 0 16 16"><rect x="1.5" y="3.5" width="13" height="9"/><path d="M1.5 3.5L8 9l6.5-5.5"/></svg>
      info@pellmorearch.com
    </li>
    <li>
      <svg viewBox="0 0 16 16"><circle cx="8" cy="8" r="6.5"/><path d="M1.5 8h13M8 1.5c-3 3.5-3 9.5 0 13M8 1.5c3 3.5 3 9.5 0 13"/></svg>
      www.pellmorearch.com
    </li>
  </ul>
</section>

</body>
</html>
```